Cutting Edge Cloud Hosting Provider needs business card design

We are a new Cloud Hosting Provider called Velkaro Hosting. (Velkaro means cloudy in Spanish.) We provide clients with virtual resources and not virtual machines directly. Our clients purchase the resources that they will use (RAM,CPU, Hard drive space) then use those resources in as many virtual machines as they like.

We are looking for a business card design that is cutting edge and hip.
Updates

The name of the company is "Velkaro Hosting". Please include the "Hosting" part of our name in the design.

Thanks

Target Market(s)

21-35 developers and I.T. Staff

Industry/Entity Type

Business

Requirements
Must have
• Rounded corners, Must Incorporate our logo, individual's name must be prominent

```html
<!DOCTYPE html>
<html lang="en">
<head>
<meta charset="utf-8">
<title>Velkaro Hosting – Business Card</title>
<link rel="stylesheet" href="https://fonts.googleapis.com/css2?family=Gelasio:wght@400&family=Open+Sans:wght@400;700&display=swap">
<style>
  :root {
    --canvas: #ffffff;
    --front-light: #c3dcee;
    --front-mid: #aecbe3;
    --front-edge: #a3c1db;
    --navy: #1f3a6b;
    --muted-blue: #7c95b8;
    --contact-blue: #2b4a7d;
    --rule: #3d5a8a;
    --card-border: #c9c9c9;
  }
  * { margin: 0; padding: 0; box-sizing: border-box; }
  html, body {
    width: 1200px;
    height: 900px;
    overflow: hidden;
    background: var(--canvas);
  }
  .presentation {
    position: relative;
    width: 1200px;
    height: 900px;
  }
  .card {
    position: absolute;
    width: 568px;
    height: 320px;
    border-radius: 10px;
  }
  .card-front {
    left: 122px;
    top: 78px;
    background: radial-gradient(ellipse at 50% 40%, var(--front-light) 0%, var(--front-mid) 55%, var(--front-edge) 100%);
    display: flex;
    align-items: center;
    justify-content: center;
  }
  .card-back {
    left: 494px;
    top: 482px;
    background: #fff;
    border: 2px solid var(--card-border);
  }
  .brand-name {
    font-family: "Open Sans", sans-serif;
    font-weight: 700;
    color: var(--navy);
    white-space: nowrap;
    letter-spacing: 0.5px;
  }
  .card-front .brand-name {
    font-size: 50px;
    margin-top: 10px;
  }
  .card-back .brand-name {
    position: absolute;
    left: 44px;
    top: 140px;
    font-size: 24px;
  }
  .divider {
    position: absolute;
    left: 274px;
    top: 92px;
    width: 2px;
    height: 124px;
    background: var(--rule);
  }
  .person {
    position: absolute;
    left: 298px;
    top: 96px;
  }
  .person-name {
    font-family: "Gelasio", serif;
    font-size: 34px;
    line-height: 1;
    color: var(--navy);
  }
  .person-title {
    font-family: "Open Sans", sans-serif;
    font-size: 13px;
    color: var(--muted-blue);
    margin-top: 4px;
  }
  .contact-list {
    list-style: none;
    position: absolute;
    left: 298px;
    top: 170px;
    font-family: "Open Sans", sans-serif;
    font-size: 15px;
    line-height: 23px;
    color: var(--contact-blue);
  }
  .contact-label { color: var(--muted-blue); margin-right: 6px; }
  .contact-label.email { margin-right: 2px; }
</style>
</head>
<body>
  <main class="presentation">
    <section class="card card-front" aria-label="Card front">
      <span class="brand-name">Velkaro Hosting</span>
    </section>

    <section class="card card-back" aria-label="Card back">
      <span class="brand-name">Velkaro Hosting</span>
      <div class="divider"></div>
      <div class="person">
        <h1 class="person-name">Marco Ellison</h1>
        <p class="person-title">Vice-President</p>
      </div>
      <ul class="contact-list">
        <li><span class="contact-label">p.</span>210.555.0142</li>
        <li><span class="contact-label">c.</span>210.555.0187</li>
        <li><span class="contact-label email">E-mail:</span>marco@velkaro.com</li>
      </ul>
    </section>
  </main>
</body>
</html>
```